Plakat-Design für IT-Systemhaus
brisk IT Solutions suchte ein neues Design in der Kategorie Plakate und hat ein Projekt auf grafikwerkhof.de gestartet.
brisk IT Solutions
The winner of our first design contests on this site. Can only say positive things about them. They work fast, respond in a timely manner and created a great design for us. Overall we're very happy with Quillwick.
Zielgruppe
Wir sind ein IT-Systemhaus mit dem Fokus auf individuelle Cloud Lösungen inkl. bester Kundenbetreuung.
Unsere primäre Zielgruppe sind Unterhnemenskunden, sprich das B2B Geschäft.
Aus der Gruppe der Unternehmenskunden interessieren uns besonders kleine und mittelständische Unternehmen.
Unser Corporate Design ist modern und dennoch auffällig gehalten.
Unsere bevorzugt Schriftart ist 'Ubuntu' bzw. 'Ubuntu Light'.
Unsere Grundfarben sind Orange (#ff8303) Grau (#747474).
Als orientierungshilfe haben wir unser Vorlage für Blöcke und Flyer mit angehangen.
Aufgabenstellung
Es handelt sich um eine Geländerwerbung (doppelseitig) zwischen einer Tankstelle und einer Straße gelegen. (Siehe Anhang)
Die Maße des Anzeitgetafel sind wie folgt: Querformat 135 x 65 (breite x höhe)
Gerne würden wir auf eine etwas provokantere Fragestellung zurückgreifen, um Aufmerksamkeit zu eregen.
Gleichzeitig möchten wir als Lösungsfinder der Fragestellung wargenommen werden.
Gut gefallen hat uns diese Lösung: https://www.grafikwerkhof.at/527190-plakat-fuer-it-systemhaus
Des Weiteren sollte die Anzeige unser Logo, Webadresse sowie unsere Telefonnummer enthalten.
Für Kreative Vorschläge sind wir dankbar.

```html
<!DOCTYPE html>
<html lang="de">
<head>
<meta charset="utf-8">
<title>brisk IT Solutions – Geländerbanner</title>
<link rel="stylesheet" href="https://fonts.googleapis.com/css2?family=Ubuntu:wght@300;400;500;700&display=swap">
<style>
  :root {
    --orange: #e5822c;
    --orange-soft: #f0b784;
    --cream: #f6ece4;
    --white: #f7f6f5;
    --grey: #747474;
    --stage: #dcdcdc;
    --photo-warm: #c99c7a;
    --photo-light: #ece4dd;
  }
  html, body {
    margin: 0;
    width: 1200px;
    height: 864px;
    overflow: hidden;
    background: var(--stage);
    font-family: "Ubuntu", sans-serif;
  }
  .banner {
    position: absolute;
    left: 20px;
    top: 142px;
    width: 1160px;
    height: 579px;
    overflow: hidden;
    background: linear-gradient(90deg, var(--orange) 0%, var(--orange-soft) 30%, var(--cream) 48%, var(--white) 60%);
  }
  .photo {
    position: absolute;
    left: 470px;
    top: 0;
    width: 690px;
    height: 579px;
    background: linear-gradient(90deg, rgba(236,228,221,0) 0%, var(--photo-light) 25%, var(--photo-warm) 65%, #3a2a24 100%);
    opacity: .55;
  }
  .shapes {
    position: absolute;
    inset: 0;
  }
  .headline {
    position: absolute;
    left: 57px;
    top: 52px;
    margin: 0;
    color: var(--white);
    font-weight: 500;
    font-size: 60px;
    line-height: 74px;
  }
  .claim {
    position: absolute;
    left: 54px;
    top: 264px;
    display: flex;
    align-items: center;
    color: var(--white);
    font-weight: 500;
  }
  .claim-brace {
    font-weight: 300;
    font-size: 110px;
    line-height: 1;
    margin-right: 8px;
  }
  .claim-text {
    font-size: 40px;
    line-height: 54px;
  }
  .brand {
    position: absolute;
    left: 52px;
    top: 478px;
    display: flex;
    align-items: center;
    gap: 12px;
    color: var(--orange);
    font-weight: 400;
    font-size: 36px;
  }
  .brand-mark {
    width: 18px;
    height: 18px;
    background: var(--grey);
  }
  .service {
    position: absolute;
    top: 441px;
    height: 53px;
    line-height: 53px;
    color: var(--white);
    font-weight: 500;
    font-size: 25px;
    text-align: center;
  }
  .contact {
    position: absolute;
    top: 507px;
    height: 57px;
    line-height: 57px;
    font-weight: 500;
    font-size: 29px;
    text-align: center;
  }
  .contact-phone { left: 362px; width: 450px; color: var(--orange); }
  .contact-web { left: 818px; width: 318px; color: var(--white); }
</style>
</head>
<body>
<section class="banner">
  <div class="photo" role="img" aria-label="Foto: frustrierte Büroangestellte hebt einen Hammer gegen einen Monitor mit der Meldung SYSTEM FAILURE"></div>

  <svg class="shapes" viewBox="0 0 1160 579" width="1160" height="579" aria-hidden="true">
    <polygon points="0,426 482,426 516,579 0,579" fill="var(--white)"/>
    <polygon points="345,441 518,441 523,494 350,494" fill="var(--orange)"/>
    <polygon points="530,441 713,441 718,494 535,494" fill="var(--orange)"/>
    <polygon points="726,441 888,441 893,494 731,494" fill="var(--orange)"/>
    <polygon points="901,441 1119,441 1124,494 906,494" fill="var(--orange)"/>
    <polygon points="357,507 820,507 823,564 363,564" fill="var(--white)"/>
    <polygon points="813,507 1130,507 1137,564 819,564" fill="var(--orange)"/>
  </svg>

  <h1 class="headline">Haben Sie Ihre<br>IT im Griff?</h1>

  <div class="claim">
    <span class="claim-brace">{</span>
    <span class="claim-text">it gemeinsam<br>optimieren.</span>
  </div>

  <div class="brand">
    <span>brisk IT Solutions</span>
    <span class="brand-mark"></span>
  </div>

  <div class="service" style="left:347px;width:174px">IT Beratung</div>
  <div class="service" style="left:532px;width:184px">IT Sicherheit</div>
  <div class="service" style="left:728px;width:163px">IT Support</div>
  <div class="service" style="left:903px;width:219px">IT Infrastruktur</div>

  <div class="contact contact-phone">Tel : +49 6123 / 58 17 40 0</div>
  <div class="contact contact-web">www.brisk-it.de</div>
</section>
</body>
</html>
```